6 - 8 'Holistic' Instagram Graphics

Hi there!
We are looking to build up a library of Graphic Templates to use as Instagram & Facebook posts for our Holistic Medi Spa (& 3 other companies eventually)
This competition is for a sample of 6 - 8 designs. For the winner(s), we will make an agreement for a batch order (Looking for 200+ designs in total), and will be looking to make a long term arrangement.
Please find a full job description in the attached Word Document.
Any questions, don't hesitate to ask.
Thanks!
Medical Spa

```html
<!DOCTYPE html>
<html lang="en">
<head>
<meta charset="utf-8">
<title>LeafHaven – Instagram Post Set</title>
<link href="https://fonts.googleapis.com/css2?family=Comfortaa:wght@300;400&family=Allura&display=swap" rel="stylesheet">
<style>
  :root {
    --page: #ffffff;
    --tile-light: #eaf6f5;
    --teal: #6fcac0;
    --teal-soft: #9dd9d7;
    --teal-dark: #1f6f6b;
    --white: #ffffff;
    --brand-grey: #a9a79a;
    --sans: 'Comfortaa', sans-serif;
    --script: 'Allura', cursive;
  }
  html, body { margin: 0; padding: 0; overflow: hidden; background: var(--page); }
  .board { position: relative; width: 1200px; height: 840px; overflow: hidden; background: var(--page); }
  .post { position: absolute; width: 213px; height: 192px; display: block; overflow: hidden; }
  .col-1 { left: 225px; } .col-2 { left: 463px; } .col-3 { left: 700px; }
  .row-1 { top: 89px; } .row-2 { top: 305px; } .row-3 { top: 522px; }
  .sans { font-family: var(--sans); font-weight: 300; }
  .script { font-family: var(--script); }
  .ink-dark { fill: var(--teal-dark); }
  .ink-teal { fill: var(--teal); }
  .ink-white { fill: var(--white); }
  .bg-light { fill: var(--tile-light); }
  .bg-teal { fill: var(--teal); }
  .bg-soft { fill: var(--teal-soft); }
  .brand { position: absolute; left: 884px; top: 748px; display: flex; align-items: center; gap: 12px; }
  .brand-dot { width: 34px; height: 34px; border-radius: 50%; background: var(--brand-grey); }
  .brand-name { font-family: var(--sans); font-weight: 400; font-size: 38px; color: var(--brand-grey); letter-spacing: -0.5px; }
</style>
</head>
<body>
<main class="board">

  <!-- Deep cleaning -->
  <svg class="post col-1 row-1" viewBox="0 0 213 192">
    <defs><linearGradient id="g-facial" x1="0" y1="0" x2="1" y2="1"><stop offset="0" stop-color="#f3d9cc"/><stop offset="1" stop-color="#d9a996"/></linearGradient></defs>
    <rect class="bg-light" width="213" height="192"/>
    <circle cx="175" cy="96" r="96" fill="url(#g-facial)" role="img" aria-label="Photo of a woman receiving a facial treatment"/>
    <text class="sans ink-dark" x="21" y="62" font-size="16">soothing,</text>
    <text class="sans ink-dark" x="21" y="82" font-size="16">deep</text>
    <text class="script ink-teal" x="20" y="110" font-size="30">cleaning</text>
  </svg>

  <!-- Make time for yourself -->
  <svg class="post col-2 row-1" viewBox="0 0 213 192">
    <rect class="bg-light" width="213" height="192"/>
    <path class="bg-teal" fill-rule="evenodd" d="M205 4 A92 92 0 1 0 205 188 A92 92 0 1 0 205 4 Z M225 26 A70 70 0 1 0 225 166 A70 70 0 1 0 225 26 Z"/>
    <text class="sans ink-dark" x="60" y="50" font-size="16" text-anchor="middle">Make</text>
    <text class="sans ink-dark" x="60" y="70" font-size="16" text-anchor="middle">time for</text>
    <text class="script ink-dark" x="60" y="100" font-size="30" text-anchor="middle">yourself</text>
  </svg>

  <!-- Eye opening meal plans -->
  <svg class="post col-3 row-1" viewBox="0 0 213 192">
    <defs><linearGradient id="g-eye" x1="0" y1="0" x2="1" y2="1"><stop offset="0" stop-color="#f0cdbb"/><stop offset="1" stop-color="#c98f78"/></linearGradient></defs>
    <rect class="bg-light" width="213" height="192"/>
    <path d="M130 0 L213 0 L213 192 L92 192 Q100 118 160 40 Z" fill="url(#g-eye)" role="img" aria-label="Close-up photo of fingers lifting the skin beside an eye"/>
    <text class="sans ink-teal" x="12" y="48" font-size="16">Eye opening</text>
    <text class="script ink-dark" x="22" y="78" font-size="28">meal plans!</text>
  </svg>

  <!-- Self-care Sunday (massage) -->
  <svg class="post col-1 row-2" viewBox="0 0 213 192">
    <defs><linearGradient id="g-massage" x1="0" y1="0" x2="1" y2="1"><stop offset="0" stop-color="#f2d6c6"/><stop offset="1" stop-color="#c78a6c"/></linearGradient></defs>
    <rect class="bg-teal" width="213" height="192"/>
    <path d="M0 192 L0 120 Q10 58 60 55 Q90 56 110 75 Q150 65 190 75 Q215 110 195 192 Z" fill="url(#g-massage)" role="img" aria-label="Photo of a man relaxing during a shoulder massage"/>
    <text class="sans ink-white" x="22" y="28" font-size="14">It's self-care</text>
    <text class="script ink-white" x="74" y="62" font-size="36">Sunday</text>
  </svg>

  <!-- Keep calm & pause -->
  <svg class="post col-2 row-2" viewBox="0 0 213 192">
    <rect class="bg-light" width="213" height="192"/>
    <path class="bg-teal" d="M115 0 L213 0 L213 180 Q160 205 98 170 Q112 115 140 75 Q110 50 115 0 Z"/>
    <text class="sans ink-teal" x="33" y="87" font-size="17">Keep calm</text>
    <text class="script ink-white" x="126" y="114" font-size="28">&amp; pause</text>
  </svg>

  <!-- Love the skin you're in -->
  <svg class="post col-3 row-2" viewBox="0 0 213 192">
    <defs><linearGradient id="g-skin" x1="0" y1="0" x2="1" y2="1"><stop offset="0" stop-color="#cfc9d2"/><stop offset="0.6" stop-color="#d9c2b8"/><stop offset="1" stop-color="#b58c7c"/></linearGradient></defs>
    <rect width="213" height="192" fill="url(#g-skin)" role="img" aria-label="Portrait photo of a woman touching her cheek"/>
    <text class="sans ink-white" x="9" y="41" font-size="17">Love the</text>
    <text class="script ink-dark" x="30" y="70" font-size="34">skin</text>
    <text class="sans ink-white" x="37" y="97" font-size="17">you're in!</text>
  </svg>

  <!-- Self-care Sunday (blossom) -->
  <svg class="post col-1 row-3" viewBox="0 0 213 192">
    <defs><linearGradient id="g-blossom" x1="0" y1="0" x2="1" y2="1"><stop offset="0" stop-color="#d9a9cf"/><stop offset="0.5" stop-color="#f1e4ee"/><stop offset="1" stop-color="#7fa256"/></linearGradient></defs>
    <rect width="213" height="121" fill="url(#g-blossom)" role="img" aria-label="Photo of pink magnolia blossoms on a branch"/>
    <rect class="bg-teal" y="121" width="213" height="71"/>
    <text class="sans ink-white" x="22" y="148" font-size="14">It's self-care</text>
    <text class="script ink-white" x="74" y="180" font-size="36">Sunday</text>
  </svg>

  <!-- Morning meditation -->
  <svg class="post col-2 row-3" viewBox="0 0 213 192">
    <defs>
      <linearGradient id="g-leaf" x1="0" y1="0" x2="1" y2="1"><stop offset="0" stop-color="#b9dcc4"/><stop offset="1" stop-color="#4f9a7c"/></linearGradient>
      <linearGradient id="g-crystal" x1="0" y1="0" x2="1" y2="1"><stop offset="0" stop-color="#ece6df"/><stop offset="1" stop-color="#9d9088"/></linearGradient>
    </defs>
    <rect class="bg-light" width="213" height="192"/>
    <path class="bg-soft" d="M0 68 Q70 60 120 125 Q160 85 213 85 L213 192 L0 192 Z"/>
    <path d="M12 100 Q70 110 100 150 L80 192 L15 192 Q2 150 12 100 Z" fill="url(#g-leaf)" role="img" aria-label="Photo of a succulent plant"/>
    <path d="M140 150 Q165 120 205 112 Q212 160 198 192 L150 192 Q135 170 140 150 Z" fill="url(#g-crystal)" role="img" aria-label="Photo of white crystals"/>
    <text class="sans ink-dark" x="34" y="40" font-size="16">Morning</text>
    <text class="script ink-dark" x="68" y="74" font-size="34">meditation</text>
  </svg>

  <!-- Beauty is health -->
  <svg class="post col-3 row-3" viewBox="0 0 213 192">
    <rect class="bg-light" width="213" height="192"/>
    <path class="bg-teal" d="M0 0 L145 0 Q160 40 190 65 Q155 100 113 192 L0 192 Z"/>
    <text class="sans ink-white" x="24" y="64" font-size="17">Beauty is health</text>
    <text class="script ink-dark" x="50" y="98" font-size="34">health</text>
    <text class="sans ink-white" x="51" y="124" font-size="17">is beauty</text>
  </svg>

  <div class="brand">
    <span class="brand-dot"></span>
    <span class="brand-name">LeafHaven</span>
  </div>
</main>
</body>
</html>
```